Valdarossi’s Artisan Pizzeria Menu Contest

I’m looking for a menu design for a new pizzeria - it’s farm to table type of restaurant - more upscale than a typical pizzeria - white washed wood interior with some industrial accents - I am looking for a creative menu layout using the attached sample menu items -
Valdarossi’s is an artisanal pizzeria with an atmosphere that will make you feel at home for any situation, first date, anniversary, business lunch, boys night out or girls night out with a menu inspired by the idea of a simple honest cooking paired with fresh – quality ingredients. Full service dining experience that is still casual but dedicated to extraordinary hospitality.
While developing the menu we have created a network of amazing farms and purveyors to supply our restaurant with fresh milled 100% California flour for our hand crafted dough, as well as sustainably farmed organic produce, meats and cheeses.
The menu includes classics like the Margherita pizza to daily seasonal specials, fresh salads to rustic small plates including moms meatball recipe to a fresh local burrata with handmade bread. Each dish reflects our passion for sourcing the freshest quality local ingredients.
To compliment the menu, Valdarossi’s serves an extensive wine list with selections focusing on Italian varietals. The cocktail program has been carefully crafted to offer something to entice ever palate and the beer list has unique selections of the world’s finest brewers.
Target Market(s)
25-45 year old men and women
Industry/Entity Type
American Restaurant
Requirements
Must have
- professional tone
Nice to have
- a balance of elegance and industrial (rustic)
Should not have
- photos or playful graphics etc..

```html
<!DOCTYPE html>
<html lang="en">
<head>
<meta charset="utf-8">
<title>Valdarossi’s Artisan Pizzeria Menu</title>
<link rel="stylesheet" href="https://fonts.googleapis.com/css2?family=Cinzel:wght@400;700&family=Lato:wght@400&display=swap">
<style>
  :root {
    --backdrop: #e9e6e1;
    --board-dark: #232323;
    --board-mid: #2f2f2f;
    --plank-line: rgba(0,0,0,0.45);
    --plank-light: rgba(255,255,255,0.04);
    --accent: #e4675b;
    --ink: #f2f0ec;
    --ink-soft: #a9a6a1;
  }
  html, body {
    margin: 0;
    padding: 0;
    width: 1200px;
    height: 798px;
    overflow: hidden;
    background: var(--backdrop);
  }
  .menu {
    position: absolute;
    left: 342px;
    top: 34px;
    width: 516px;
    height: 729px;
    background: linear-gradient(180deg, var(--board-mid), var(--board-dark));
    box-shadow: 0 6px 18px rgba(0,0,0,0.25);
    overflow: hidden;
    color: var(--ink);
    font-family: "Cinzel", serif;
  }
  .planks {
    position: absolute;
    inset: 0;
    width: 100%;
    height: 100%;
  }
  .section-title {
    position: absolute;
    margin: 0;
    font-family: "Cinzel", serif;
    font-weight: 700;
    font-size: 25px;
    letter-spacing: 3px;
    color: var(--accent);
  }
  .pizza-title { left: 36px; top: 134px; }
  .crusts-title { left: 330px; top: 238px; }
  .dips-title { left: 346px; top: 517px; }

  .item-list {
    position: absolute;
    margin: 0;
    padding: 0;
    list-style: none;
  }
  .pizza-list { left: 36px; top: 182px; width: 216px; }
  .crust-list { left: 276px; top: 282px; width: 204px; }
  .dip-list { left: 276px; top: 574px; width: 204px; }

  .item {
    position: relative;
    height: 39px;
  }
  .crust-list .item { height: 30px; }
  .dip-list .item { height: 20px; }

  .item-name {
    display: block;
    font-size: 13px;
    font-weight: 700;
    letter-spacing: 1.2px;
    text-transform: uppercase;
    line-height: 15px;
    padding-right: 48px;
    white-space: nowrap;
  }
  .dip-list .item-name { font-size: 12px; font-weight: 400; line-height: 16px; }
  .item-price {
    position: absolute;
    right: 0;
    top: 0;
    font-family: "Lato", sans-serif;
    font-size: 12px;
    line-height: 15px;
    letter-spacing: 0.5px;
  }
  .item-desc {
    display: block;
    font-family: "Lato", sans-serif;
    font-size: 8px;
    line-height: 11px;
    color: var(--ink-soft);
    white-space: nowrap;
  }

  .brand {
    position: absolute;
    left: 276px;
    top: 66px;
    width: 201px;
    text-align: center;
  }
  .brand-name {
    display: block;
    font-family: "Cinzel", serif;
    font-weight: 700;
    font-size: 27px;
    letter-spacing: 1px;
    color: var(--ink);
    line-height: 34px;
  }
  .brand-tagline {
    display: block;
    margin-top: 2px;
    font-family: "Lato", sans-serif;
    font-size: 9px;
    letter-spacing: 3px;
    text-transform: uppercase;
    color: var(--ink-soft);
  }
</style>
</head>
<body>
  <main class="menu">
    <svg class="planks" viewBox="0 0 516 729" preserveAspectRatio="none" aria-hidden="true">
      <g stroke="var(--plank-line)" stroke-width="2">
        <line x1="57" y1="0" x2="57" y2="729"/>
        <line x1="118" y1="0" x2="118" y2="729"/>
        <line x1="176" y1="0" x2="176" y2="729"/>
        <line x1="238" y1="0" x2="238" y2="729"/>
        <line x1="297" y1="0" x2="297" y2="729"/>
        <line x1="356" y1="0" x2="356" y2="729"/>
        <line x1="417" y1="0" x2="417" y2="729"/>
        <line x1="470" y1="0" x2="470" y2="729"/>
      </g>
      <g stroke="var(--plank-light)" stroke-width="1">
        <line x1="59" y1="0" x2="59" y2="729"/>
        <line x1="120" y1="0" x2="120" y2="729"/>
        <line x1="178" y1="0" x2="178" y2="729"/>
        <line x1="240" y1="0" x2="240" y2="729"/>
        <line x1="299" y1="0" x2="299" y2="729"/>
        <line x1="358" y1="0" x2="358" y2="729"/>
        <line x1="419" y1="0" x2="419" y2="729"/>
        <line x1="472" y1="0" x2="472" y2="729"/>
      </g>
    </svg>

    <header class="brand">
      <span class="brand-name">Valdarossi’s</span>
      <span class="brand-tagline">Artisan Pizzeria</span>
    </header>

    <h2 class="section-title pizza-title">Pizza</h2>
    <ul class="item-list pizza-list">
      <li class="item"><span class="item-name">Margherita</span><span class="item-price">14.00</span><span class="item-desc">Tomato, fior di latte, basil</span></li>
      <li class="item"><span class="item-name">Organic Sausage</span><span class="item-price">16.00</span><span class="item-desc">Fennel sausage, onion, mozzarella, sage</span></li>
      <li class="item"><span class="item-name">Pepperoni</span><span class="item-price">15.00</span><span class="item-desc">Cup pepperoni, tomato, oregano, parmesan</span></li>
      <li class="item"><span class="item-name">Salumi and Burrata</span><span class="item-price">17.00</span><span class="item-desc">Salami, fresh burrata, chili, honey</span></li>
      <li class="item"><span class="item-name">Daily Special</span><span class="item-price">18.00</span><span class="item-desc">Ask about today’s seasonal pie</span></li>
      <li class="item"><span class="item-name">Mushroom</span><span class="item-price">15.00</span><span class="item-desc">Wild mushrooms, thyme, garlic, fontina</span></li>
      <li class="item"><span class="item-name">Prosciutto and Egg</span><span class="item-price">16.00</span><span class="item-desc">Prosciutto, farm egg, arugula, pecorino</span></li>
      <li class="item"><span class="item-name">Quattro Formaggi</span><span class="item-price">16.00</span><span class="item-desc">Mozzarella, gorgonzola, fontina, parmesan</span></li>
      <li class="item"><span class="item-name">Farmers Pizza</span><span class="item-price">17.00</span><span class="item-desc">Market vegetables, ricotta, pesto drizzle</span></li>
      <li class="item"><span class="item-name">Keto Friendly</span><span class="item-price">18.00</span><span class="item-desc">Cauliflower crust, sausage, peppers, cheese</span></li>
    </ul>

    <h2 class="section-title crusts-title">Crusts</h2>
    <ul class="item-list crust-list">
      <li class="item"><span class="item-name">Traditional</span><span class="item-price">0.00</span><span class="item-desc">Hand stretched California flour dough</span></li>
      <li class="item"><span class="item-name">Gluten Free</span><span class="item-price">2.00</span><span class="item-desc">Rice and tapioca flour base</span></li>
      <li class="item"><span class="item-name">Cauliflower</span><span class="item-price">3.00</span><span class="item-desc">Low carb cauliflower and egg</span></li>
    </ul>

    <h2 class="section-title dips-title">Dips</h2>
    <ul class="item-list dip-list">
      <li class="item"><span class="item-name">Ranch</span><span class="item-price">2.00</span></li>
      <li class="item"><span class="item-name">Tomato Sauce</span><span class="item-price">2.00</span></li>
      <li class="item"><span class="item-name">Spicy Dip</span><span class="item-price">2.00</span></li>
      <li class="item"><span class="item-name">Blue Cheese</span><span class="item-price">2.00</span></li>
    </ul>
  </main>
</body>
</html>
```